Book cover for the book Where the Lantern Hums Before the Morning

I need a book cover for a book that explains that the mind, or consciousness, is the basis of reality. We live in a dream. This mind is all that exists. We have experiences in this dream. They are all in the mind. I see a tree, but the tree isn't outside in the world. It is an experience of sight wholly in the mind. The cover must not have brains. The mind is not in the brain. The brain is in the mind. We, as part of the universal intelligence, are creating this dream reality moment by moment. The cover doesn't have to show a mind creating a landscape, but that is one approach. It just has to be exciting and enticing. The big bang is really a big thought. I found a fascinating graphic I've attached as just an example. I also attach a page that I made that is dull just go give another approach. I want something much better.

```html
<!DOCTYPE html>
<html lang="en">
<head>
<meta charset="utf-8">
<title>Where the Lantern Hums Before the Morning — Book Cover</title>
<link rel="stylesheet" href="https://fonts.googleapis.com/css2?family=EB+Garamond:wght@400;500&display=swap">
<style>
  :root {
    --paper: #ecebe6;
    --ink: #0d0d0d;
    --teal: #006b63;
    --on-teal: #f2f1ec;
  }
  html, body {
    margin: 0;
    padding: 0;
    overflow: hidden;
    background: var(--paper);
  }
  .cover {
    position: relative;
    width: 800px;
    height: 1200px;
    overflow: hidden;
    background: var(--paper);
    font-family: "EB Garamond", Garamond, serif;
  }
  .title {
    position: absolute;
    top: 58px;
    left: 0;
    width: 800px;
    margin: 0;
    text-align: center;
    font-weight: 400;
    font-size: 84px;
    line-height: 97px;
    letter-spacing: 0.5px;
  }
  .title-line { display: block; }
  .title-line--dark { color: var(--ink); }
  .title-line--accent { color: var(--teal); }
  .author {
    position: absolute;
    top: 502px;
    left: 271px;
    width: 249px;
    height: 35px;
    background: var(--teal);
    color: var(--on-teal);
    font-size: 25px;
    line-height: 35px;
    text-align: center;
    letter-spacing: 0.3px;
  }
  .scene-art {
    position: absolute;
    top: 576px;
    left: 50px;
    width: 700px;
    height: 624px;
  }
</style>
</head>
<body>
  <main class="cover">
    <h1 class="title">
      <span class="title-line title-line--dark">Where the</span>
      <span class="title-line title-line--dark">Lantern Hums</span>
      <span class="title-line title-line--accent">Before the</span>
      <span class="title-line title-line--accent">Morning</span>
    </h1>

    <div class="author">R. Elliot Marsh, PhD</div>

    <svg class="scene-art" viewBox="0 0 700 624" role="img"
         aria-label="Watercolour illustration: a person in a blue hoodie and a pale dog sit from behind, facing a green river scene framed by a dark stone arch">
      <defs>
        <radialGradient id="sceneWash" cx="50%" cy="45%" r="60%">
          <stop offset="0%" stop-color="#7fa85a"/>
          <stop offset="40%" stop-color="#5f8a4c"/>
          <stop offset="72%" stop-color="#4a4a3e"/>
          <stop offset="100%" stop-color="#a9a598" stop-opacity="0.6"/>
        </radialGradient>
      </defs>
      <path fill="url(#sceneWash)"
            d="M40 200 C60 90 200 20 360 18 C520 16 640 90 670 200
               C700 300 690 420 650 500 C610 580 520 620 400 622
               L280 622 C170 615 80 560 45 470 C15 390 20 290 40 200 Z"/>
    </svg>
  </main>
</body>
</html>
```